HOT TUB - SPAS service needs an business card

I need an business for my company who his specialise in a maintenance,water treatment and cleaning of Hot Tub - Spas for commercial and residential customers. The company operate mainly in the ski resort of Chamonix, Megève and St Gervais. The final product should communicate pure water, cleanest and professional for luxury property's.
I have upload a logo but any improvement on it is welcome.(color,size, details etc..) or any other idea. Thank you
Company Name: 58 BAINS
My name: Laurent Mazeyrac
Email: lmazey@courrielo.fr
Tel: +33 (0)6 81 52 29 07
Description to be on the card in french(first langage) and in English:
- Spas service
- Entretien, traitement eau, nettoyage.
- Maintenance, water treatment, cleaning.

```html
<!DOCTYPE html>
<html lang="fr">
<head>
<meta charset="utf-8">
<title>58 BAINS – Business card</title>
<link rel="stylesheet" href="https://fonts.googleapis.com/css2?family=Roboto+Condensed:wght@700&family=Roboto:wght@300;400&display=swap">
<style>
  :root {
    --backdrop: #a3a3a3;
    --card-white: #f8fbff;
    --ink: #111111;
    --ice-blue: #3aaee6;
    --rule: #333333;
    --snow-light: #eef6fc;
    --snow-mid: #b9dcf2;
    --snow-deep: #6fb0da;
  }
  * { box-sizing: border-box; margin: 0; padding: 0; }
  html, body {
    width: 1200px; height: 900px; overflow: hidden;
    background: var(--backdrop);
  }
  .stage {
    width: 1200px; height: 900px;
    display: flex; align-items: center; justify-content: center; gap: 40px;
  }
  .card {
    position: relative;
    width: 540px; height: 350px;
    background: var(--card-white);
    overflow: hidden;
    box-shadow: 0 6px 18px rgba(0,0,0,0.25);
  }

  /* Front: identity side */
  .card-front { display: flex; align-items: center; }
  .brand-mark {
    width: 220px; display: flex; align-items: center; justify-content: center; gap: 10px;
    padding-left: 30px;
  }
  .brand-name {
    font-family: "Roboto Condensed", "Arial Narrow", sans-serif;
    font-weight: 700; font-size: 50px; letter-spacing: 1px;
    color: var(--ink); line-height: 1;
  }
  .brand-dot { width: 14px; height: 14px; border-radius: 50%; background: var(--ice-blue); flex: none; }
  .divider { width: 1px; height: 150px; background: var(--rule); margin: 0 26px 0 24px; align-self: center; transform: translateY(-10px); }
  .contact { font-family: "Roboto", Helvetica, sans-serif; color: var(--ink); transform: translateY(-22px); }
  .contact-name { font-weight: 300; font-size: 26px; margin-bottom: 10px; }
  .contact-line { font-weight: 400; font-size: 16px; margin-bottom: 8px; }
  .contact-label { color: var(--ice-blue); margin-right: 4px; }

  /* Back: services side */
  .card-back { background: var(--snow-light); }
  .scene-photo {
    position: absolute; inset: 0;
    background:
      radial-gradient(ellipse at 70% 15%, #ffffff 0%, rgba(255,255,255,0) 45%),
      linear-gradient(170deg, var(--snow-mid) 0%, #dff0fb 35%, var(--snow-deep) 70%, #cfe7f7 100%);
  }
  .services {
    position: absolute; left: 40px;
    font-family: "Roboto Condensed", "Arial Narrow", sans-serif;
    font-weight: 700; font-size: 17px; color: var(--ink);
    line-height: 1.5;
  }
  .services-fr { top: 70px; }
  .services-en { top: 215px; }
  .back-brand {
    position: absolute; right: 30px; top: 120px;
    display: flex; align-items: center; gap: 10px;
  }
  .back-brand .brand-name { font-size: 46px; }
</style>
</head>
<body>
<main class="stage">
  <section class="card card-front" aria-label="Recto">
    <div class="brand-mark">
      <span class="brand-dot"></span>
      <span class="brand-name">58 BAINS</span>
    </div>
    <div class="divider"></div>
    <div class="contact">
      <p class="contact-name">Laurent Mazeyrac</p>
      <p class="contact-line"><span class="contact-label">E:</span>lmazey@courrielo.fr</p>
      <p class="contact-line"><span class="contact-label">T:</span>+33 (0)6 81 52 29 07</p>
    </div>
  </section>

  <section class="card card-back" aria-label="Verso">
    <div class="scene-photo" role="img" aria-label="Photo of an outdoor hot tub beside a snowy wooden chalet with mountains and pine trees under a bright winter sky"></div>
    <ul class="services services-fr" style="list-style:none">
      <li>- Service de Spas</li>
      <li>- Entretien, traitement eau, nettoyage</li>
    </ul>
    <ul class="services services-en" style="list-style:none">
      <li>- Spas service</li>
      <li>- Maintenance, water treatment, cleaning</li>
    </ul>
    <div class="back-brand">
      <span class="brand-dot"></span>
      <span class="brand-name">58 BAINS</span>
    </div>
  </section>
</main>
</body>
</html>
```